Plastic Business Card for Bookkeeper

We are looking for a simple professional business card design to use for printing on thin frosted plastic (see-through) card stock. Logo and brand guideline documents are attached as well as a photo of our old business card, and another business card example that we like.

Target Market(s)

Small Business

Industry/Entity Type

Bookkeeper

Contact Information for Business Card

Harriet Valdez CPA
Chief Executive Bookkeeper
T. 03 5926 4187
M. 0432 861 507
E. harriet@quillpathledger.com
W. www.quillpathledger.com

Font styles to use
Sans Serif

Colors
6b449b
00a990

Requirements
Must have
• Stick with logo colors. Writing should be clear and easy to read and not too cramped together.
Nice to have
• Tag line for back of the card - 'Not your ordinary Bookkeeper'

```html
<!DOCTYPE html>
<html lang="en">
<head>
<meta charset="utf-8">
<title>Quillpath Ledger – Business Card</title>
<link rel="stylesheet" href="https://fonts.googleapis.com/css2?family=Roboto:wght@400;500;700&display=swap">
<style>
  :root {
    --backdrop: #d9d6d2;
    --card: #f3f3f1;
    --card-edge: #e2e2df;
    --teal-ink: #17606b;
    --purple: #5b3d8c;
    --text: #2e2e33;
  }
  * { margin: 0; padding: 0; box-sizing: border-box; }
  html, body {
    width: 1200px;
    height: 969px;
    overflow: hidden;
    background: var(--backdrop);
    font-family: "Roboto", Arial, sans-serif;
  }
  .canvas {
    position: relative;
    width: 1200px;
    height: 969px;
  }
  .card {
    position: absolute;
    left: 141px;
    top: 223px;
    width: 918px;
    height: 523px;
    background: var(--card);
    border: 1px solid var(--card-edge);
    border-radius: 26px;
    box-shadow: 0 10px 30px rgba(0,0,0,0.12);
  }
  .brand {
    position: absolute;
    left: 80px;
    top: 0;
    width: 330px;
    height: 100%;
    display: flex;
    flex-direction: column;
    align-items: center;
    justify-content: center;
    gap: 14px;
    color: var(--purple);
    font-weight: 500;
    text-transform: uppercase;
    text-align: center;
  }
  .brand-dot {
    width: 22px;
    height: 22px;
    border-radius: 50%;
    background: var(--purple);
  }
  .brand-name {
    font-size: 25px;
    letter-spacing: 1px;
    line-height: 1.3;
  }
  .divider {
    position: absolute;
    left: 412px;
    top: 155px;
    width: 16px;
    height: 212px;
  }
  .details {
    position: absolute;
    left: 467px;
    top: 160px;
  }
  .person-name {
    font-size: 32px;
    font-weight: 700;
    color: var(--teal-ink);
    letter-spacing: 0.2px;
  }
  .person-title {
    font-size: 21px;
    font-weight: 700;
    color: var(--purple);
    margin-top: 2px;
  }
  .contacts {
    list-style: none;
    margin-top: 22px;
  }
  .contacts li {
    display: flex;
    align-items: center;
    gap: 12px;
    font-size: 21px;
    color: var(--text);
    height: 30px;
  }
  .contacts svg {
    width: 22px;
    height: 22px;
    fill: var(--teal-ink);
    flex: none;
  }
</style>
</head>
<body>
<div class="canvas">
  <section class="card">
    <div class="brand">
      <span class="brand-dot"></span>
      <span class="brand-name">Quillpath<br>Ledger</span>
    </div>

    <svg class="divider" viewBox="0 0 16 212" aria-hidden="true">
      <line x1="8" y1="10" x2="8" y2="212" stroke="#5b3d8c" stroke-width="2.5"/>
      <polygon points="8,0 14,12 2,12" fill="#5b3d8c"/>
    </svg>

    <div class="details">
      <h1 class="person-name">Harriet Valdez CPA</h1>
      <p class="person-title">Chief Executive Bookkeeper</p>
      <ul class="contacts">
        <li>
          <svg viewBox="0 0 24 24" aria-hidden="true"><path d="M6.6 10.8c1.4 2.8 3.8 5.1 6.6 6.6l2.2-2.2c.3-.3.7-.4 1-.2 1.1.4 2.3.6 3.6.6.6 0 1 .4 1 1V20c0 .6-.4 1-1 1C10.6 21 3 13.4 3 4c0-.6.4-1 1-1h3.5c.6 0 1 .4 1 1 0 1.3.2 2.5.6 3.6.1.3 0 .7-.2 1z"/></svg>
          03 5926 4187
        </li>
        <li>
          <svg viewBox="0 0 24 24" aria-hidden="true"><path d="M7 1h10c1.1 0 2 .9 2 2v18c0 1.1-.9 2-2 2H7c-1.1 0-2-.9-2-2V3c0-1.1.9-2 2-2zm0 3v14h10V4zm5 15.5a1.2 1.2 0 1 0 0 2.4 1.2 1.2 0 0 0 0-2.4z"/></svg>
          0432 861 507
        </li>
        <li>
          <svg viewBox="0 0 24 24" aria-hidden="true"><path d="M3 6h18v12H3zm2 2v.5l7 4.5 7-4.5V8l-7 4.5z"/></svg>
          harriet@quillpathledger.com
        </li>
        <li>
          <svg viewBox="0 0 24 24" aria-hidden="true"><circle cx="12" cy="12" r="9.5"/></svg>
          www.quillpathledger.com
        </li>
      </ul>
    </div>
  </section>
</div>
</body>
</html>
```